The Perfect Business Card for PineHarbor

I am looking for a business card which beautifully incorporates my logo, reflects my business and looks special, elegant and clean.

```html
<!DOCTYPE html>
<html lang="en">
<head>
<meta charset="UTF-8">
<title>PineHarbor Business Card</title>
<link rel="stylesheet" href="https://fonts.googleapis.com/css2?family=Montserrat:wght@400;500;700;800&display=swap">
<style>
  :root {
    --backdrop: #3b3c3f;
    --card: #1a1a1b;
    --green: #7aa33c;
    --text: #ffffff;
  }
  * { box-sizing: border-box; margin: 0; padding: 0; }
  html, body {
    width: 1200px; height: 887px; overflow: hidden;
    background: var(--backdrop);
    font-family: "Montserrat", sans-serif;
  }
  .stage {
    position: relative; width: 1200px; height: 887px;
    display: flex; align-items: center; justify-content: center; gap: 40px;
  }
  .card {
    position: relative; width: 540px; height: 309px;
    background: var(--card); border-radius: 22px; overflow: hidden;
  }
  .brand {
    position: absolute; display: flex; align-items: center; gap: 12px;
    color: var(--green); font-weight: 500; letter-spacing: 0.5px;
  }
  .brand-dot {
    width: 38px; height: 38px; border: 2px solid var(--green); border-radius: 50%;
  }
  .card-back .brand { left: 50%; top: 50%; transform: translate(-50%, -50%); font-size: 40px; }
  .card-back .brand-dot { width: 48px; height: 48px; }
  .card-front .brand { right: 34px; top: 62px; font-size: 28px; }

  .accent-bar {
    position: absolute; left: 26px; top: 122px; width: 12px; height: 48px;
    background: var(--green);
  }
  .identity { position: absolute; left: 52px; top: 116px; }
  .person-name {
    color: var(--green); font-weight: 800; font-size: 19px; letter-spacing: 0.3px;
    text-transform: uppercase;
  }
  .person-role { color: var(--text); font-weight: 500; font-size: 20px; margin-top: 2px; }
  .rule { position: absolute; left: 66px; height: 2px; background: var(--green); }
  .rule-top { top: 183px; width: 220px; }
  .rule-bottom { top: 236px; width: 240px; }
  .address {
    position: absolute; left: 66px; top: 192px;
    color: var(--text); font-size: 13px; line-height: 18px;
  }
  .contacts {
    position: absolute; left: 66px; top: 244px; list-style: none;
    color: var(--text); font-size: 12.5px; line-height: 19px;
  }
  .contacts li { display: flex; align-items: center; gap: 8px; }
  .contacts svg { width: 12px; height: 12px; fill: var(--green); flex: none; }
</style>
</head>
<body>
<main class="stage">
  <section class="card card-back">
    <div class="brand"><span class="brand-dot"></span><span>PineHarbor</span></div>
  </section>

  <section class="card card-front">
    <div class="brand"><span class="brand-dot"></span><span>PineHarbor</span></div>
    <div class="accent-bar"></div>
    <div class="identity">
      <p class="person-name">Dalen Whitcombe</p>
      <p class="person-role">Co-Founder</p>
    </div>
    <div class="rule rule-top"></div>
    <p class="address">Harborview Plaza 1820 Cedar Lane<br>Suite 310</p>
    <div class="rule rule-bottom"></div>
    <ul class="contacts">
      <li>
        <svg viewBox="0 0 24 24"><path d="M6.6 10.8a15.1 15.1 0 0 0 6.6 6.6l2.2-2.2a1 1 0 0 1 1-.25 11.4 11.4 0 0 0 3.6.6 1 1 0 0 1 1 1V20a1 1 0 0 1-1 1A17 17 0 0 1 3 4a1 1 0 0 1 1-1h3.5a1 1 0 0 1 1 1c0 1.25.2 2.45.6 3.6a1 1 0 0 1-.25 1z"/></svg>
        <span>(555) 204-7781</span>
      </li>
      <li>
        <svg viewBox="0 0 24 24"><path d="M2 5h20v14H2zm2 2v.4l8 5 8-5V7zm0 2.8V17h16V9.8l-8 5z"/></svg>
        <span>hello@pineharborco.com</span>
      </li>
      <li>
        <svg viewBox="0 0 24 24"><path d="M12 2a10 10 0 1 0 0 20 10 10 0 0 0 0-20zm6.9 6h-3a15 15 0 0 0-1.3-3.9A8 8 0 0 1 18.9 8zM12 4c.8 1.2 1.5 2.5 1.9 4h-3.8c.4-1.5 1.1-2.8 1.9-4zM4.3 14a8 8 0 0 1 0-4h3.4a16 16 0 0 0 0 4zm.8 2h3a15 15 0 0 0 1.3 3.9A8 8 0 0 1 5.1 16zm3-8h-3a8 8 0 0 1 4.3-3.9A15 15 0 0 0 8.1 8zM12 20c-.8-1.2-1.5-2.5-1.9-4h3.8c-.4 1.5-1.1 2.8-1.9 4zm2.3-6H9.7a14 14 0 0 1 0-4h4.6a14 14 0 0 1 0 4zm.3 5.9a15 15 0 0 0 1.3-3.9h3a8 8 0 0 1-4.3 3.9zm1.7-5.9a16 16 0 0 0 0-4h3.4a8 8 0 0 1 0 4z"/></svg>
        <span>www.pineharborco.com</span>
      </li>
    </ul>
  </section>
</main>
</body>
</html>
```